Falcrest security business card

Looking for a business card for my security company

Target Market(s)

Security

Industry/Entity Type

Security

Contact Information for Business Card

Name - Gil Marston. Title - General manager - direct 314 862.4490 website www. falcrestsecurityservices.example email - gil@ falcrestsecurityservices.example

Requirements
Must have
• Logo attached

```html
<!DOCTYPE html>
<html lang="en">
<head>
<meta charset="utf-8">
<title>Falcrest Security Services – Business Card</title>
<link rel="stylesheet" href="https://fonts.googleapis.com/css2?family=Montserrat:wght@400;500;700&display=swap">
<style>
  :root {
    --backdrop: #2a2a2a;
    --card-black: #050505;
    --gold: #d6a941;
    --gold-deep: #a97c22;
    --pattern-light: #8a8a8a;
    --pattern-dark: #1a1a1a;
    --text-white: #f2f2f2;
    --rule: #6d6450;
  }
  * { margin: 0; padding: 0; box-sizing: border-box; }
  html, body {
    width: 1200px; height: 1186px; overflow: hidden;
    background: var(--backdrop);
    font-family: "Montserrat", sans-serif;
  }
  .stage {
    position: relative; width: 1200px; height: 1186px;
  }
  .card {
    position: absolute; left: 260px; width: 680px; height: 390px;
    background: var(--card-black);
    border: 3px solid var(--gold);
    border-radius: 26px;
    overflow: hidden;
  }
  .card--back { top: 150px; }
  .card--front { top: 620px; }

  .pattern-field {
    position: absolute; inset: 0;
    background: linear-gradient(120deg, var(--pattern-light) 0%, #4a4a4a 35%, var(--pattern-dark) 75%, #2b2b2b 100%);
  }

  .brand {
    position: absolute; right: 70px; top: 70px;
    display: flex; align-items: center; gap: 14px;
  }
  .brand__mark {
    width: 30px; height: 30px; border-radius: 50%;
    background: var(--gold);
  }
  .brand__name {
    font-weight: 700; font-size: 58px; letter-spacing: 1px;
    color: var(--gold); text-transform: uppercase;
  }
  .brand-rule {
    position: absolute; left: 290px; right: 70px; top: 170px;
    height: 1px; background: var(--rule);
  }

  .holder {
    position: absolute; left: 50px; bottom: 48px; width: 560px;
  }
  .holder__name {
    font-weight: 700; font-size: 32px; color: var(--gold);
    line-height: 1.1;
  }
  .holder__title {
    font-weight: 400; font-size: 17px; color: var(--text-white);
    margin-top: 6px;
  }
  .holder__rule {
    height: 1px; background: var(--rule); margin: 16px 0 14px; width: 520px;
  }
  .contact {
    list-style: none; display: grid; gap: 10px;
  }
  .contact__item {
    display: flex; align-items: center; gap: 14px;
    font-size: 17px; color: var(--text-white);
  }
  .contact__icon { width: 16px; height: 16px; flex: none; }
</style>
</head>
<body>
<main class="stage">
  <section class="card card--back">
    <div class="pattern-field" role="img" aria-label="Repeating pattern of silver leaping big-cat silhouettes on black"></div>
  </section>

  <section class="card card--front">
    <div class="brand">
      <span class="brand__mark"></span>
      <span class="brand__name">Falcrest</span>
    </div>
    <div class="brand-rule"></div>

    <div class="holder">
      <h1 class="holder__name">Gil Marston</h1>
      <p class="holder__title">General manager</p>
      <div class="holder__rule"></div>
      <ul class="contact">
        <li class="contact__item">
          <svg class="contact__icon" viewBox="0 0 24 24" aria-hidden="true">
            <path fill="#d6a941" d="M6.6 10.8a15.1 15.1 0 0 0 6.6 6.6l2.2-2.2a1 1 0 0 1 1-.25 11.4 11.4 0 0 0 3.6.57 1 1 0 0 1 1 1V20a1 1 0 0 1-1 1A17 17 0 0 1 3 4a1 1 0 0 1 1-1h3.5a1 1 0 0 1 1 1c0 1.25.2 2.45.57 3.57a1 1 0 0 1-.25 1z"/>
          </svg>
          <span>314 862.4490</span>
        </li>
        <li class="contact__item">
          <svg class="contact__icon" viewBox="0 0 24 24" aria-hidden="true">
            <circle cx="12" cy="12" r="9.5" fill="none" stroke="#d6a941" stroke-width="2"/>
            <path d="M2.5 12h19M12 2.5c3 3 3 16 0 19M12 2.5c-3 3-3 16 0 19" fill="none" stroke="#d6a941" stroke-width="1.6"/>
          </svg>
          <span>www.falcrestsecurityservices.example</span>
        </li>
      </ul>
    </div>
  </section>
</main>
</body>
</html>
```